Sales Flyer Advertising Aircraft Sales & Acquisitions

Looking for very professional flyer that can also be converted and sent as an email. Something simple but very high end. Maybe a line on there about taking advantage of 80% tax deduction before it drops this year. Don’t want it to seem too salesy but also catch the eye and get the message across. My website is www.quillonaerospan.com to give you an idea. It is in the process of being reworked but it’s something to go off of.

```html
<!DOCTYPE html>
<html lang="en">
<head>
<meta charset="utf-8">
<title>Quillon Aerospan Services – Aircraft Sales &amp; Acquisitions</title>
<link rel="stylesheet" href="https://fonts.googleapis.com/css2?family=Poppins:wght@400;500;600;700&family=Source+Sans+3:ital,wght@0,400;0,600;0,700;1,600&display=swap">
<style>
  :root {
    --ink: #0d0d0d;
    --paper: #ffffff;
    --sky: #dbe9f7;
    --sky-deep: #b9d3ee;
    --dusk: #f08a2e;
    --haze: #8e9298;
    --tarmac: #2a2a2a;
    --footer-top: #0a0a0a;
    --footer-bottom: #3a3838;
    --text-dark: #1a1a1a;
  }
  * { box-sizing: border-box; margin: 0; padding: 0; }
  html, body { width: 902px; height: 1200px; overflow: hidden; background: #ffffff; }
  .flyer {
    position: relative;
    width: 902px; height: 1200px;
    background: var(--ink);
    overflow: hidden;
    font-family: "Source Sans 3", sans-serif;
    color: var(--text-dark);
  }
  .hero-photo {
    position: absolute; left: 0; top: 0; width: 902px; height: 600px;
    background:
      linear-gradient(180deg, rgba(0,0,0,0) 0%, rgba(0,0,0,0) 50%, rgba(30,30,30,0.85) 72%, var(--ink) 100%),
      linear-gradient(100deg, var(--dusk) 0%, #e9a062 30%, #a9a7a4 55%, var(--haze) 100%);
  }
  .shapes { position: absolute; left: 0; top: 0; }
  .sky { fill: url(#skyFill); }
  .footer-band { fill: url(#footerFill); }
  .swoosh { fill: none; stroke: var(--paper); }

  .brand {
    position: absolute; left: 46px; top: 58px;
    display: flex; align-items: center; gap: 12px;
  }
  .brand-dot { width: 34px; height: 34px; border-radius: 50%; background: var(--ink); }
  .brand-name {
    font-family: "Poppins", sans-serif; font-weight: 600;
    font-size: 17px; letter-spacing: 1px; color: var(--ink);
  }

  .offer { position: absolute; left: 40px; top: 386px; width: 240px; text-align: center; }
  .offer-lead { font-family: "Poppins", sans-serif; font-weight: 500; font-size: 17px; letter-spacing: .5px; color: var(--ink); }
  .offer-figure { font-family: "Poppins", sans-serif; font-weight: 700; font-size: 100px; line-height: 92px; color: var(--ink); letter-spacing: -2px; }
  .offer-band {
    display: inline-block; margin-top: 4px;
    background: var(--ink); color: var(--paper);
    font-family: "Poppins", sans-serif; font-weight: 500; font-size: 21px;
    padding: 0 8px; line-height: 28px;
  }
  .offer-note { margin-top: 8px; font-family: "Poppins", sans-serif; font-size: 12.5px; font-weight: 500; letter-spacing: .3px; color: var(--ink); }

  .headline { position: absolute; left: 354px; top: 516px; width: 470px; }
  .headline-main {
    font-family: "Poppins", sans-serif; font-weight: 500; font-size: 86px; line-height: 86px;
    color: var(--paper); letter-spacing: 1px;
  }
  .headline-sub {
    margin-top: 2px;
    background: var(--paper); color: var(--ink);
    font-family: "Poppins", sans-serif; font-weight: 500; font-size: 39px; line-height: 64px;
    padding-left: 10px; white-space: nowrap;
  }

  .service { position: absolute; left: 38px; width: 420px; }
  .service-sales { top: 636px; }
  .service-acq { top: 856px; }
  .service-tag { display: flex; align-items: center; }
  .service-icon {
    width: 40px; height: 40px; border-radius: 50%; background: var(--ink);
    border: 2px solid var(--paper); box-shadow: 0 0 0 1px var(--ink);
    display: flex; align-items: center; justify-content: center; position: relative; z-index: 1;
  }
  .service-title {
    margin-left: -12px; padding: 0 22px 0 24px;
    background: var(--ink); color: var(--paper);
    font-family: "Poppins", sans-serif; font-weight: 500; font-size: 16px; line-height: 26px;
    border-radius: 0 14px 14px 0;
  }
  .service-question { margin-top: 14px; font-style: italic; font-weight: 600; font-size: 17px; color: var(--ink); }
  .service-copy { margin-top: 10px; font-size: 13.5px; font-weight: 600; line-height: 17px; width: 340px; color: var(--text-dark); }
  .service-copy + .service-copy { margin-top: 12px; }
  .service-acq .service-copy:first-of-type { margin-top: 18px; }

  .extras { position: absolute; left: 582px; top: 798px; }
  .extras-title { font-family: "Poppins", sans-serif; font-weight: 500; font-size: 16px; color: var(--ink); }
  .extras-list { list-style: none; margin-top: 18px; margin-left: -6px; }
  .extras-list li { display: flex; align-items: center; gap: 12px; font-size: 14px; font-weight: 600; height: 29px; color: var(--ink); }

  .contact { position: absolute; left: 0; top: 1060px; width: 902px; height: 140px; color: var(--paper); }
  .contact-label { position: absolute; left: 32px; top: 46px; font-family: "Poppins", sans-serif; font-size: 27px; font-weight: 400; }
  .contact-lines { position: absolute; left: 232px; top: 26px; }
  .contact-line { display: flex; align-items: center; gap: 10px; font-size: 14.5px; height: 26px; }
  .contact-line.phone { font-family: "Poppins", sans-serif; font-weight: 600; font-size: 21px; height: 34px; }
  .contact-divider { position: absolute; left: 476px; top: 8px; width: 1px; height: 116px; background: rgba(255,255,255,.5); }
  .contact-place { position: absolute; left: 520px; top: 30px; display: flex; gap: 12px; }
  .contact-address { font-size: 14px; font-weight: 600; line-height: 17px; }
  .contact-social { position: absolute; left: 552px; top: 82px; display: flex; align-items: center; gap: 8px; font-size: 15px; font-weight: 600; }
  .social-dot { width: 28px; height: 28px; border-radius: 50%; border: 1.5px solid var(--paper); }
</style>
</head>
<body>
<main class="flyer">
  <div class="hero-photo" role="img" aria-label="Photo of a white twin turboprop aircraft parked on an airport apron at dusk, orange sky fading to grey"></div>

  <svg class="shapes" width="902" height="1200" viewBox="0 0 902 1200" aria-hidden="true">
    <defs>
      <linearGradient id="skyFill" x1="0" y1="0" x2="1" y2="1">
        <stop offset="0" stop-color="#e8f1fa"/>
        <stop offset=".6" stop-color="var(--sky)"/>
        <stop offset="1" stop-color="var(--sky-deep)"/>
      </linearGradient>
      <linearGradient id="footerFill" x1="0" y1="0" x2="0" y2="1">
        <stop offset="0" stop-color="var(--footer-top)"/>
        <stop offset="1" stop-color="var(--footer-bottom)"/>
      </linearGradient>
    </defs>
    <path class="sky" d="M0,352 C40,326 120,316 190,320 C262,324 332,350 340,410 C348,470 300,520 330,560 C352,592 302,612 292,628 C322,640 346,662 338,692 C330,732 420,762 460,800 C480,820 492,792 520,760 C560,702 640,690 700,704 C760,716 780,680 832,680 C872,680 902,700 902,722 L902,1080 L0,1080 Z"/>
    <line x1="476" y1="812" x2="476" y2="1030" stroke="#ffffff" stroke-opacity=".7" stroke-width="1"/>
    <path class="swoosh" stroke-width="6" d="M0,1002 C160,1040 360,1046 530,1008 C690,972 830,892 902,806"/>
    <path class="footer-band" d="M0,1016 C160,1054 360,1062 530,1024 C690,988 832,906 902,826 L902,1200 L0,1200 Z"/>
  </svg>

  <header class="brand">
    <span class="brand-dot"></span>
    <span class="brand-name">QUILLON AEROSPAN SERVICES</span>
  </header>

  <section class="offer">
    <p class="offer-lead">TAKE ADVANTAGE OF</p>
    <p class="offer-figure">80%</p>
    <p class="offer-band">TAX DEDUCTION</p>
    <p class="offer-note">BEFORE IT DROPS THIS YEAR</p>
  </section>

  <h1 class="headline">
    <span class="headline-main">AIRCRAFT</span>
    <span class="headline-sub" style="display:block">Sales &amp; Acquisitions</span>
  </h1>

  <section class="service service-sales">
    <div class="service-tag">
      <span class="service-icon">
        <svg width="22" height="16" viewBox="0 0 22 16"><path d="M3,2 H15 L20,8 L15,14 H3 Z" fill="none" stroke="#fff" stroke-width="1.6"/><circle cx="15" cy="8" r="1.4" fill="#fff"/></svg>
      </span>
      <h2 class="service-title">AIRCRAFT SALES</h2>
    </div>
    <p class="service-question">Looking to sell your aircraft?</p>
    <p class="service-copy">Let Quillon Aerospan handle the transaction on your behalf.</p>
    <p class="service-copy">We walk with you step by step through the entire process and are readily available to answer questions along the way.</p>
  </section>

  <section class="service service-acq">
    <div class="service-tag">
      <span class="service-icon">
        <svg width="18" height="20" viewBox="0 0 18 20"><rect x="2" y="1" width="12" height="17" rx="1" fill="none" stroke="#fff" stroke-width="1.6"/><line x1="5" y1="6" x2="11" y2="6" stroke="#fff" stroke-width="1.4"/><line x1="5" y1="10" x2="11" y2="10" stroke="#fff" stroke-width="1.4"/><line x1="5" y1="14" x2="9" y2="14" stroke="#fff" stroke-width="1.4"/></svg>
      </span>
      <h2 class="service-title">AIRCRAFT ACQUISITIONS</h2>
    </div>
    <p class="service-copy">Whether you are a first-time purchaser or a frequent buyer, having proper representation is invaluable.</p>
    <p class="service-copy">From sourcing off market leads to negotiating prices to match your budget, Quillon Aerospan is ready to handle your purchase.</p>
  </section>

  <section class="extras">
    <h2 class="extras-title">OUR OTHER SERVICES:</h2>
    <ul class="extras-list">
      <li><svg width="14" height="12" viewBox="0 0 14 12"><path d="M1,6 L5,10 L13,1" fill="none" stroke="#0d0d0d" stroke-width="2.4"/></svg>Pre-Purchase Inspections</li>
      <li><svg width="14" height="12" viewBox="0 0 14 12"><path d="M1,6 L5,10 L13,1" fill="none" stroke="#0d0d0d" stroke-width="2.4"/></svg>Ferry Pilot Services</li>
      <li><svg width="14" height="12" viewBox="0 0 14 12"><path d="M1,6 L5,10 L13,1" fill="none" stroke="#0d0d0d" stroke-width="2.4"/></svg>Aircraft Management</li>
    </ul>
  </section>

  <footer class="contact">
    <p class="contact-label">Contact Us :</p>
    <div class="contact-lines">
      <p class="contact-line phone">
        <svg width="16" height="16" viewBox="0 0 16 16"><path d="M3,1 L6,1 L7,5 L5,6.5 C6,9 7,10 9.5,11 L11,9 L15,10 L15,13 C15,14 14,15 13,15 C7,15 1,9 1,3 C1,2 2,1 3,1 Z" fill="none" stroke="#fff" stroke-width="1.3"/></svg>
        +1 555.014.2290
      </p>
      <p class="contact-line">
        <svg width="15" height="11" viewBox="0 0 15 11"><rect x=".7" y=".7" width="13.6" height="9.6" fill="none" stroke="#fff" stroke-width="1.2"/><path d="M1,1 L7.5,6 L14,1" fill="none" stroke="#fff" stroke-width="1.2"/></svg>
        dana@quillonaerospan.com
      </p>
      <p class="contact-line">
        <svg width="14" height="14" viewBox="0 0 14 14"><circle cx="7" cy="7" r="6" fill="none" stroke="#fff" stroke-width="1.2"/><ellipse cx="7" cy="7" rx="2.6" ry="6" fill="none" stroke="#fff" stroke-width="1.1"/><line x1="1" y1="7" x2="13" y2="7" stroke="#fff" stroke-width="1.1"/></svg>
        www.quillonaerospan.com
      </p>
    </div>
    <span class="contact-divider"></span>
    <div class="contact-place">
      <svg width="16" height="22" viewBox="0 0 16 22"><path d="M8,21 C8,21 1,12 1,7.5 C1,3.5 4,1 8,1 C12,1 15,3.5 15,7.5 C15,12 8,21 8,21 Z" fill="none" stroke="#fff" stroke-width="1.4"/><circle cx="8" cy="7.5" r="2.4" fill="none" stroke="#fff" stroke-width="1.4"/></svg>
      <p class="contact-address">Marlow Field Airport<br>Eastbrook Florida, 32000</p>
    </div>
    <div class="contact-social">
      <span>Follow us on :</span>
      <span class="social-dot"></span>
      <span class="social-dot"></span>
    </div>
  </footer>
</main>
</body>
</html>
```